Professional CPA firm wants card to tell our clients why employees are wearing jeans today

We are a professional CPA firm and want to allow our employees the choice to wear jeans instead of professional attire for the day at the cost of contributing $2.00 to a collection jar for a local charity - at the end of a six month period the firm will donate the money collected from the employees to the local charity

HI - We are located in a town called Auburn - instead of the copy saying "local charity", I'd like it to reference that it will go to an "Auburn centered charity"

thanks!                                   

It Professional

```html
<!DOCTYPE html>
<html lang="en">
<head>
<meta charset="utf-8">
<title>Supporting the Community – Hartwell, Lane &amp; Carver</title>
<link rel="stylesheet" href="https://fonts.googleapis.com/css2?family=Lato:wght@400;700&display=swap">
<style>
  :root {
    --denim-light: #6f9fc4;
    --denim-mid: #5c8db5;
    --denim-dark: #4a7aa3;
    --seam-band: #7aaed6;
    --thread: #e9dcc0;
    --thread-shadow: #3c4f5e;
    --tag-teal: #1fb0cf;
    --tag-teal-dark: #138fae;
    --tag-strip: #e6f4f8;
    --card-white: #ffffff;
    --stitch-brown: #5a4a38;
    --ink-blue: #1c5a92;
  }
  html, body {
    margin: 0;
    padding: 0;
    overflow: hidden;
  }
  .canvas {
    position: relative;
    width: 1200px;
    height: 960px;
    overflow: hidden;
    font-family: "Lato", Arial, sans-serif;
  }
  .denim-texture {
    position: absolute;
    inset: 0;
    background: linear-gradient(180deg, var(--denim-mid) 0%, var(--denim-light) 45%, var(--denim-mid) 100%);
  }
  .seams {
    position: absolute;
    inset: 0;
  }
  .brand-tag {
    position: absolute;
    left: 717px;
    top: 197px;
    width: 350px;
    height: 136px;
    background: linear-gradient(180deg, var(--tag-teal) 0%, var(--tag-teal-dark) 100%);
    border-radius: 0 0 14px 14px;
    box-shadow: 0 4px 8px rgba(0,0,0,0.35);
    display: flex;
    align-items: center;
    padding-left: 62px;
    box-sizing: border-box;
  }
  .brand-tag::before {
    content: "";
    position: absolute;
    left: 26px;
    top: 0;
    bottom: 14px;
    width: 14px;
    background: var(--tag-strip);
  }
  .brand-name {
    color: #ffffff;
    font-weight: 400;
    font-size: 25px;
    white-space: nowrap;
  }
  .notice-card {
    position: absolute;
    left: 108px;
    top: 387px;
    width: 1005px;
    height: 433px;
    background: var(--card-white);
    box-sizing: border-box;
    padding: 22px 50px 0 47px;
  }
  .notice-card svg {
    position: absolute;
    inset: 0;
  }
  .notice-title {
    position: relative;
    margin: 0 0 14px;
    color: var(--ink-blue);
    font-size: 42px;
    font-weight: 700;
    line-height: 56px;
    text-decoration: underline;
    text-decoration-thickness: 3px;
    text-underline-offset: 6px;
  }
  .notice-body {
    position: relative;
    margin: 0;
    max-width: 905px;
    color: var(--ink-blue);
    font-size: 35px;
    font-weight: 700;
    line-height: 47px;
  }
</style>
</head>
<body>
<div class="canvas">
  <div class="denim-texture" role="img" aria-label="Blue denim fabric texture"></div>

  <svg class="seams" width="1200" height="960" viewBox="0 0 1200 960" aria-hidden="true">
    <rect x="0" y="68" width="1200" height="130" fill="var(--seam-band)" opacity="0.55"/>
    <rect x="0" y="188" width="1200" height="10" fill="var(--denim-dark)" opacity="0.6"/>
    <line x1="0" y1="97" x2="1200" y2="97" stroke="var(--thread-shadow)" stroke-width="6" stroke-dasharray="22 8" opacity="0.5"/>
    <line x1="0" y1="95" x2="1200" y2="95" stroke="var(--thread)" stroke-width="4" stroke-dasharray="22 8"/>
    <line x1="0" y1="182" x2="1200" y2="182" stroke="var(--thread-shadow)" stroke-width="6" stroke-dasharray="22 8" opacity="0.5"/>
    <line x1="0" y1="180" x2="1200" y2="180" stroke="var(--thread)" stroke-width="4" stroke-dasharray="22 8"/>
    <rect x="0" y="835" width="1200" height="48" fill="var(--seam-band)" opacity="0.45"/>
  </svg>

  <div class="brand-tag">
    <span class="brand-name">Hartwell, Lane &amp; Carver</span>
  </div>

  <div class="notice-card">
    <svg width="1005" height="433" viewBox="0 0 1005 433" aria-hidden="true">
      <rect x="12" y="12" width="981" height="409" fill="none" stroke="var(--stitch-brown)" stroke-width="4" stroke-dasharray="16 7"/>
    </svg>
    <h1 class="notice-title">Supporting the Community</h1>
    <p class="notice-body">&nbsp;We wish to advise our valued customers that we have offered our employees the choice to wear jeans in exchange for a small donation earmarked for an Auburn centered charity.&nbsp; You can depend on the same level of professional service you have come to expect.</p>
  </div>
</div>
</body>
</html>
```